Billboard Design for Equipment Rental Business

We need a billboard design for our equipment rental business called Brindlewood Equipment Company. We are based in Georgia. We rent construction tools, equipment, and dumpsters. We currently have a design but feel like we could get something better. Our phone number is 912-730-2591 and our website is www.brindlewoodequipment-example.com

```html
<!DOCTYPE html>
<html lang="en">
<head>
<meta charset="utf-8">
<title>Brindlewood Equipment Company – Billboard</title>
<link rel="stylesheet" href="https://fonts.googleapis.com/css2?family=Anton&family=Montserrat:wght@600&family=Oswald:wght@600&display=swap">
<style>
  :root {
    --page-bg-top: #a9a9a9;
    --page-bg-bottom: #bdbdbd;
    --yellow-top: #f9e619;
    --yellow-bottom: #f7b71f;
    --ink: #111111;
    --band-black: #121212;
    --band-orange: #f7a21f;
    --white: #ffffff;
    --photo-sky: #b9d2ea;
    --photo-mid: #e39a3a;
    --photo-sand: #b89068;
  }
  * { margin: 0; padding: 0; box-sizing: border-box; }
  html, body {
    width: 706px;
    height: 1200px;
    overflow: hidden;
  }
  body {
    background: linear-gradient(180deg, var(--page-bg-top), var(--page-bg-bottom));
    position: relative;
  }
  .billboard {
    position: absolute;
    left: 23px;
    top: 380px;
    width: 660px;
    height: 440px;
    background: linear-gradient(180deg, var(--yellow-top) 0%, var(--yellow-bottom) 100%);
    box-shadow: 0 14px 22px rgba(0,0,0,0.28);
    overflow: hidden;
  }
  .billboard-shapes {
    position: absolute;
    inset: 0;
    width: 660px;
    height: 440px;
  }
  .headline {
    position: absolute;
    left: 31px;
    top: 20px;
    font-family: "Anton", sans-serif;
    font-weight: 400;
    font-size: 62px;
    line-height: 60px;
    color: var(--ink);
    text-transform: uppercase;
    letter-spacing: 0.5px;
  }
  .headline span { display: block; }
  .intro {
    position: absolute;
    left: 31px;
    top: 208px;
    width: 290px;
    font-family: "Montserrat", sans-serif;
    font-weight: 600;
    font-size: 14.5px;
    line-height: 18px;
    letter-spacing: -0.3px;
    color: var(--ink);
  }
  .divider {
    position: absolute;
    left: 32px;
    top: 281px;
    width: 242px;
    height: 1px;
    background: var(--ink);
  }
  .brand {
    position: absolute;
    left: 32px;
    top: 296px;
    display: flex;
    align-items: center;
    gap: 12px;
  }
  .brand-mark {
    width: 40px;
    height: 40px;
    border: 2px solid var(--ink);
    border-radius: 50%;
    flex: none;
  }
  .brand-name {
    font-family: "Oswald", sans-serif;
    font-weight: 600;
    font-size: 20px;
    line-height: 22px;
    text-transform: uppercase;
    color: var(--ink);
    width: 200px;
    letter-spacing: 0.5px;
  }
  .phone {
    position: absolute;
    left: 30px;
    top: 380px;
    height: 60px;
    display: flex;
    align-items: center;
    font-family: "Anton", sans-serif;
    font-size: 44px;
    color: var(--white);
    letter-spacing: 0.5px;
  }
  .website {
    position: absolute;
    left: 350px;
    width: 298px;
    top: 380px;
    height: 60px;
    display: flex;
    align-items: center;
    justify-content: center;
    font-family: "Anton", sans-serif;
    font-size: 16px;
    color: var(--ink);
    letter-spacing: 0;
    white-space: nowrap;
    overflow: hidden;
  }
</style>
</head>
<body>
  <main class="billboard">
    <svg class="billboard-shapes" viewBox="0 0 660 440" xmlns="http://www.w3.org/2000/svg">
      <defs>
        <linearGradient id="photo-tones" x1="0" y1="0" x2="0" y2="1">
          <stop offset="0" stop-color="var(--photo-sky)"/>
          <stop offset="0.45" stop-color="#d9c3a6"/>
          <stop offset="0.6" stop-color="var(--photo-mid)"/>
          <stop offset="1" stop-color="var(--photo-sand)"/>
        </linearGradient>
      </defs>
      <polygon class="accent-stripe" points="420,0 452,0 360,222 344,232" fill="var(--band-black)"/>
      <polygon class="hero-photo" role="img" aria-label="Orange tracked excavator with a dirt-covered bucket on a sandy construction site under a partly cloudy sky"
               points="452,0 660,0 660,378 296,378" fill="url(#photo-tones)"/>
      <rect class="band-rule" x="0" y="375" width="660" height="3" fill="var(--white)"/>
      <polygon class="band-black" points="0,378 314,378 337,440 0,440" fill="var(--band-black)"/>
      <polygon class="band-gap" points="314,378 320,378 343,440 337,440" fill="var(--white)"/>
      <polygon class="band-orange" points="320,378 660,378 660,440 343,440" fill="var(--band-orange)"/>
    </svg>

    <h1 class="headline">
      <span>Tools</span>
      <span>Equipment</span>
      <span>Dumpsters</span>
    </h1>

    <p class="intro">We are based in Georgia. We rent construction tools, equipment, and dumpsters.</p>

    <div class="divider"></div>

    <div class="brand">
      <div class="brand-mark"></div>
      <div class="brand-name">Brindlewood Equipment Company</div>
    </div>

    <div class="phone">912-730-2591</div>
    <div class="website">www.brindlewoodequipment-example.com</div>
  </main>
</body>
</html>
```